Healthcare website - Diabetic Shoes - Elderfund - No Cost

I am looking to upgrade my website. I do not want to use Wordpress, Adobe Muse or another designing program. The code should be easily editable using textpad or VI. After the project is done I want to easily add my custom PHP code.

Features
Creative and Modern Design .
Fully responsive site for use on mobile devices
bootstrap, jquery

My current website is
www.pebblewalkco.com

Target Market(s)

Older people who have diabetes. Target market is +60 years old, but we do have younger people going to the site to help out their parents.

Industry/Entity Type

Healthcare

Coding

Coded - Design and coding required

Number of Pages Required

2 page

Colors

Designer to choose colors to be used in the design.

Requirements
Must have
• The code should be easily editable using textpad or VI. After the project is done I want to easily add my custom PHP code.
• The first page will be the home page and the other page I need is this form.
• https://www.pebblewalkco.com/pebble-walk-co-do-i-qualify.php
Should not have
• I do not want to use Wordpress, Adobe Muse or another designing program.

```html
<!DOCTYPE html>
<html lang="en">
<head>
<meta charset="utf-8">
<title>Pebble Walk Co – Diabetic Shoes Covered by Elderfund</title>
<link href="https://fonts.googleapis.com/css2?family=Ubuntu:wght@300;400;500;700&display=swap" rel="stylesheet">
<style>
:root{
  --green:#6cc04a;
  --green-dark:#58a83a;
  --blue:#3d6fa6;
  --blue-dark:#2f5c8e;
  --ink:#222;
  --text:#777;
  --grey-bg:#eef0f2;
  --white:#fff;
  --red:#e32b24;
}
*{box-sizing:border-box;margin:0;padding:0}
html,body{width:1200px;height:4604px;overflow:hidden}
body{font-family:'Ubuntu',sans-serif;color:var(--ink);background:var(--white);position:relative}
.abs{position:absolute}
a{color:inherit;text-decoration:none}

/* top bar */
.topbar{top:0;left:0;width:1200px;height:44px;background:var(--blue);color:#fff;font-size:15px;font-weight:500;z-index:5}
.topbar .follow{left:76px;top:13px}
.dot{display:inline-block;width:24px;height:24px;border-radius:50%;background:var(--green)}
.topbar .socials{left:186px;top:10px;display:flex;gap:8px}
.topbar .phone{left:715px;top:10px;display:flex;align-items:center;gap:8px;white-space:nowrap}
.pill{display:inline-flex;align-items:center;gap:6px;background:var(--green);border-radius:14px;padding:5px 14px;font-size:13px}
.topbar .login{left:885px;top:8px}
.topbar .chat{left:990px;top:8px}

/* nav */
.nav{top:44px;left:0;width:1200px;height:86px;background:#fff;z-index:5}
.brand{display:flex;align-items:center;gap:10px;font-weight:500;font-size:30px;color:var(--green);white-space:nowrap}
.nav .brand{left:76px;top:24px}
.nav ul{list-style:none;display:flex;left:330px;top:0;height:86px;align-items:center;font-size:13px;font-weight:500;color:#444;white-space:nowrap}
.nav li{padding:0 11px;height:86px;display:flex;align-items:center}
.nav li.active{background:var(--green);color:#fff;padding:0 14px}

/* hero */
.hero{top:130px;left:0;width:1200px;height:550px;overflow:hidden;background:#fff}
.hero-photo{left:0;top:0;width:640px;height:550px}
.hero h1{left:577px;top:80px;width:560px;font-size:46px;line-height:1.12;font-weight:700;color:#111}
.hero p{left:577px;top:255px;width:500px;font-size:17px;line-height:1.45;color:#444}
.dots{display:flex;gap:8px}
.dots span{width:12px;height:12px;border-radius:50%;border:2px solid #9aa;background:#fff}
.dots span.on{background:var(--blue);border-color:var(--blue)}
.hero .dots{left:556px;top:512px}

/* about */
.about{top:680px;left:0;width:1200px;height:400px;z-index:3}
.video{left:77px;top:63px;width:383px;height:240px;background:linear-gradient(135deg,#d9dee3,#a8b3be);border:2px solid #ccc}
.watch{left:120px;top:313px;display:flex;align-items:center;gap:14px;color:var(--red);font-weight:700;font-size:18px;white-space:nowrap}
.play{width:52px;height:52px;border-radius:50%;background:var(--red);display:flex;align-items:center;justify-content:center}
.title{font-weight:500;text-transform:uppercase;letter-spacing:.5px}
.about h2{left:516px;top:55px;font-size:44px;color:var(--green);white-space:nowrap}
.about .copy{left:516px;top:118px;width:610px;font-size:13px;line-height:1.55;color:#999}
.about .copy p{margin-bottom:12px}
.btn{display:inline-block;background:var(--green);color:#fff;border-radius:30px;font-weight:500;text-transform:uppercase;text-align:center;white-space:nowrap}
.about .btn{left:516px;top:318px;width:186px;height:56px;line-height:56px;font-size:18px}

/* steps */
.steps{top:1040px;left:0;width:1200px;height:680px;background:linear-gradient(180deg,#f4f5f6,#e6e9ec)}
.steps-curve{top:1040px;left:0;width:1200px;height:110px}
.steps h2{top:150px;left:0;width:1200px;text-align:center;font-size:40px;color:var(--blue)}
.steps h3{top:205px;left:0;width:1200px;text-align:center;font-size:32px;color:var(--green)}
.steps-diagram{left:420px;top:270px;width:360px;height:360px}
.step{width:230px;font-size:15px;line-height:1.45;color:#333}
.step .ic{display:block;width:56px;height:64px;margin-bottom:8px}

/* catalog */
.catalog{top:1720px;left:0;width:1200px;height:300px;background:var(--green)}
.catalog h2{top:48px;left:0;width:1200px;text-align:center;font-size:40px;color:var(--blue)}
.catalog h2 span{color:#fff}
.field{height:48px;background:#fff;font-size:13px;color:#888;padding:0 12px;display:flex;align-items:center;justify-content:space-between;white-space:nowrap}
.field .caret{width:30px;height:48px;margin-right:-12px;background:var(--blue);display:flex;align-items:center;justify-content:center}
.catalog .send{border:2px solid #fff;border-radius:26px;color:#fff;font-size:17px;height:48px;line-height:44px;text-align:center;text-transform:uppercase}

/* feature rows */
.feature{left:0;width:1200px;overflow:hidden}
.feature h2{font-size:42px;font-weight:500;text-transform:uppercase;white-space:nowrap}
.feature h3{font-size:36px;font-weight:400;text-transform:uppercase;white-space:nowrap}
.feature p{font-size:14px;line-height:1.6}
.round-photo{border-radius:50%;border:10px solid #fff;box-shadow:0 0 0 2px #d8dde2}
.f1{top:2020px;height:420px;background:linear-gradient(90deg,#fff 0%,#fff 60%,#eceff2 100%)}
.f2{top:2440px;height:415px;background:linear-gradient(180deg,#365a86,#4d7fb2 55%,#27476c)}
.f3{top:2855px;height:415px;background:linear-gradient(90deg,#fff,#fff 60%,#eef0f3)}

/* shoes */
.shoe-band{top:3270px;left:0;width:1200px;height:215px;background:var(--green);text-align:center}
.shoe-band h2{position:absolute;top:60px;width:1200px;font-size:42px;color:var(--blue)}
.shoe-band h3{position:absolute;top:120px;width:1200px;font-size:28px;color:#fff}
.shoes{top:3485px;left:0;width:1200px;height:420px;background:linear-gradient(180deg,#e4e7ea,#f4f5f6)}
.shoe{width:220px;text-align:center;font-size:13px;color:#222}
.shoe .img{width:200px;height:150px;margin:0 auto 14px;border-radius:40px 60px 20px 20px}
.shoe b{display:block;font-weight:500}

/* products */
.products{top:3870px;left:0;width:1200px;height:520px}
.products h2{top:105px;left:0;width:1200px;text-align:center;font-size:42px;color:var(--blue)}
.products h3{top:158px;left:0;width:1200px;text-align:center;font-size:30px;color:var(--green)}
.product h4{font-size:22px;font-weight:500;color:var(--blue);margin-bottom:10px}
.product p{font-size:14px;line-height:1.6;color:#888;width:250px}

/* footer */
.footer{top:4390px;left:0;width:1200px;height:214px;background:var(--blue);color:#fff}
.footer ul{list-style:none;display:flex;gap:22px;right:80px;top:52px;font-size:15px;font-weight:500;white-space:nowrap}
.footer .copy{right:80px;top:82px;font-size:14px}
.footer .brand{left:76px;top:150px;color:#fff;font-size:44px}
.footer .socials{right:80px;top:136px;display:flex;gap:14px}
.footer .socials .dot{width:46px;height:46px}
</style>
</head>
<body>

<div class="topbar abs">
  <span class="follow abs">Follow Us On</span>
  <span class="socials abs"><i class="dot"></i><i class="dot"></i></span>
  <span class="phone abs"><i class="dot" style="display:flex;align-items:center;justify-content:center"><svg width="12" height="12" viewBox="0 0 24 24"><path fill="#fff" d="M6.6 10.8a15 15 0 0 0 6.6 6.6l2.2-2.2c.3-.3.7-.4 1-.2 1.1.4 2.3.6 3.6.6.6 0 1 .4 1 1V20c0 .6-.4 1-1 1A17 17 0 0 1 3 4c0-.6.4-1 1-1h3.5c.6 0 1 .4 1 1 0 1.3.2 2.5.6 3.6.1.3 0 .7-.2 1z"/></svg></i>1-800-555-0142</span>
  <span class="pill login abs">LOGIN</span>
  <span class="pill chat abs">LIVE CHAT</span>
</div>

<header class="nav abs">
  <a class="brand abs" href="#"><i class="dot" style="width:26px;height:26px"></i>Pebble Walk Co</a>
  <ul class="abs">
    <li class="active">HOME</li>
    <li>PEBBLE WALK CO! DO I QUALIFY</li>
    <li>WHY DIABETIC SHOES</li>
    <li>SHOES</li>
    <li>PRODUCTS</li>
    <li>SHOE FITTER JOBS</li>
    <li>FAQ</li>
  </ul>
</header>

<section class="hero abs">
  <svg class="abs" style="left:0;top:0" width="1200" height="550" aria-hidden="true">
    <polygon points="0,0 540,0 740,550 0,550" fill="#3d6fa6"/>
    <polygon points="540,0 600,0 800,550 740,550" fill="#dfe6ee" opacity=".6"/>
    <polygon points="720,550 1200,330 1200,550" fill="#6cc04a"/>
    <polygon points="780,550 1200,400 1200,550" fill="#5cb53c"/>
  </svg>
  <div class="hero-photo abs" role="img" aria-label="Brown diabetic walking shoe with orange laces" style="background:radial-gradient(ellipse 42% 30% at 40% 50%,#9b7a56 0%,#7d6146 45%,rgba(61,111,166,0) 75%)"></div>
  <h1 class="abs">DIABETIC SHOES OR SNEAKERS COVERED BY ELDERFUND</h1>
  <p class="abs">No or little out of pocket Cost To You! Elderfund, and most insurance plans, may cover the cost of one pair of diabetic shoes and three pairs of custom inserts per calendar year.</p>
  <div class="dots abs"><span></span><span></span><span class="on"></span><span></span></div>
</section>

<section class="about abs">
  <div class="video abs" role="img" aria-label="Video still of a presenter explaining shoe coverage"></div>
  <div class="watch abs"><span class="play"><svg width="20" height="20" viewBox="0 0 20 20"><path d="M6 3l11 7-11 7z" fill="#fff"/></svg></span>WATCH VIDEO FULL WIDTH</div>
  <h2 class="title abs">About Pebble Walk Co</h2>
  <div class="copy abs">
    <p>Pebble Walk Co was created by Harbor Medical Supply to educate clients and prospective shoe fitters about diabetic shoes and the coverage that Elderfund provides. Founded by a board-certified podiatrist, the company's mission is to help clients receive properly fitted shoes from qualified healthcare professionals around the United States. Harbor Medical Supply works directly with Elderfund to determine the patient's coverage.</p>
    <p>Pebble Walk Co was created by Harbor Medical Supply to educate clients and prospective shoe fitters about diabetic shoes and the coverage that Elderfund provides.</p>
  </div>
  <a class="btn abs" href="#">Know More</a>
</section>

<section class="steps abs">
  <div class="abs" style="left:0;top:0;width:1200px;height:680px;opacity:.35" role="img" aria-label="Faded row of sneakers in the background"></div>
  <h2 class="title abs">4 Easy Steps to Receive Your</h2>
  <h3 class="title abs">New Therapeutic Shoes</h3>
  <svg class="steps-diagram abs" viewBox="0 0 360 360" aria-hidden="true">
    <circle cx="180" cy="180" r="160" fill="#fff" stroke="#3d6fa6" stroke-width="12"/>
    <circle cx="180" cy="180" r="84" fill="#6cc04a"/>
    <g fill="#fff" stroke="#3d6fa6" stroke-width="8">
      <circle cx="67" cy="67" r="26"/><circle cx="293" cy="67" r="26"/>
      <circle cx="67" cy="293" r="26"/><circle cx="293" cy="293" r="26"/>
    </g>
    <g fill="#6cc04a"><circle cx="67" cy="67" r="14"/><circle cx="293" cy="67" r="14"/><circle cx="67" cy="293" r="14"/><circle cx="293" cy="293" r="14"/></g>
  </svg>
  <div class="step abs" style="left:170px;top:300px;text-align:right">
    <svg class="ic" viewBox="0 0 56 64" style="margin-left:auto"><path d="M4 2h34l14 14v46H4z" fill="none" stroke="#6cc04a" stroke-width="4"/><path d="M14 26h28M14 36h28M14 46h20" stroke="#6cc04a" stroke-width="4"/></svg>
    Fill Out An Application To See If You Qualify.
  </div>
  <div class="step abs" style="left:800px;top:300px">
    <svg class="ic" viewBox="0 0 80 50" style="width:90px;height:56px"><path d="M4 30c10 0 20-10 30-20 10 8 24 12 40 14v14H4z" fill="#6cc04a"/><rect x="4" y="40" width="70" height="6" fill="#58a83a"/></svg>
    Enjoy Your New Shoes!
  </div>
  <div class="step abs" style="left:150px;top:500px;text-align:right;width:250px">
    <svg class="ic" viewBox="0 0 56 64" style="margin-left:auto"><rect x="8" y="6" width="40" height="52" rx="4" fill="none" stroke="#6cc04a" stroke-width="4"/><path d="M18 30l8 8 14-16" fill="none" stroke="#6cc04a" stroke-width="4"/></svg>
    After The Prescription Is Signed, a Certified Shoe Fitter Will fit Your New Shoes.
  </div>
  <div class="step abs" style="left:800px;top:500px">
    <svg class="ic" viewBox="0 0 64 64"><circle cx="14" cy="12" r="8" fill="#6cc04a"/><circle cx="50" cy="12" r="8" fill="#6cc04a"/><path d="M6 62V26h16v36M42 62V26h16v36" fill="#6cc04a"/><rect x="24" y="28" width="16" height="12" fill="#58a83a"/></svg>
    A Prescription Will Be Faxed To your Primary Physician.
  </div>
</section>
<svg class="steps-curve abs" viewBox="0 0 1200 110" preserveAspectRatio="none" aria-hidden="true"><path d="M0 0h1200v30Q600 150 0 30z" fill="#fff"/></svg>

<section class="catalog abs">
  <h2 class="title abs">Request a Free <span>Diabetic Shoe Catalog</span></h2>
  <div class="field abs" style="left:77px;top:130px;width:250px">Name*</div>
  <div class="field abs" style="left:337px;top:130px;width:250px">Email*</div>
  <div class="field abs" style="left:597px;top:130px;width:250px">Phone*</div>
  <div class="field abs" style="left:857px;top:130px;width:266px">Address**</div>
  <div class="field abs" style="left:77px;top:186px;width:250px">Primary Insurance**<span class="caret"><svg width="12" height="8"><path d="M0 0h12L6 8z" fill="#fff"/></svg></span></div>
  <div class="field abs" style="left:337px;top:186px;width:250px">Check eligibility Online?*<span class="caret"><svg width="12" height="8"><path d="M0 0h12L6 8z" fill="#fff"/></svg></span></div>
  <div class="field abs" style="left:597px;top:186px;width:250px">Comments**</div>
  <div class="send abs" style="left:872px;top:186px;width:250px">Request Catalog</div>
</section>

<section class="feature f1 abs">
  <div class="round-photo abs" role="img" aria-label="Close-up of a foot being examined" style="left:105px;top:40px;width:290px;height:290px;background:radial-gradient(circle,#f1d6c6,#b7c6d3)"></div>
  <h2 class="abs" style="left:485px;top:120px;color:var(--blue)">How Does Diabetes Cause</h2>
  <h3 class="abs" style="left:485px;top:172px;color:var(--green)">Foot Problems ?</h3>
  <p class="abs" style="left:485px;top:225px;width:640px;color:#999">Diabetes can cause neuropathy (nerve damage), which reduces feeling in your feet. This makes you less likely to feel the early warning signs of foot problems. Decreased circulation reduces the ability to heal and fight off infection. These two conditions significantly increase the likelihood of foot complications, infection, and ulceration.</p>
</section>

<section class="feature f2 abs">
  <div class="abs" role="img" aria-label="Runner's legs on a seaside path" style="left:0;top:0;width:1200px;height:415px;background:linear-gradient(180deg,rgba(120,160,200,.3),rgba(30,60,100,.35))"></div>
  <h2 class="abs" style="left:77px;top:95px;color:#fff">Why Are Properly Fitted</h2>
  <h3 class="abs" style="left:77px;top:148px;color:var(--green)">Shoes Important ?</h3>
  <p class="abs" style="left:77px;top:200px;width:660px;color:#e6edf5">Twenty four million people have diabetes, and twenty-five percent of this population will develop foot problems caused by their disease. We provide the most fashionable orthopedic shoes available, in a variety of styles and brands, to help treat and prevent painful diabetic symptoms.</p>
  <div class="round-photo abs" role="img" aria-label="Blue and white running shoe" style="left:800px;top:55px;width:300px;height:300px;background:radial-gradient(circle,#6fc4ea,#cfd8de);box-shadow:0 0 0 3px #6b8fb5"></div>
</section>

<section class="feature f3 abs">
  <div class="round-photo abs" role="img" aria-label="Purple shoe on a pink surface" style="left:100px;top:75px;width:290px;height:290px;background:radial-gradient(circle,#7a4fa8,#c53a8d 70%,#3a3a3a)"></div>
  <h2 class="abs" style="left:485px;top:105px;color:var(--blue)">How Do You Know If Ortho-</h2>
  <h3 class="abs" style="left:485px;top:157px;color:var(--blue)">pedic Are Right For You ?</h3>
  <p class="abs" style="left:485px;top:210px;width:650px;color:#999">Anyone with Diabetic Neuropathy, poor circulation, high risk of infection or nerve damage can benefit from diabetic socks and our shoes. Elderfund patients who qualify are eligible for one pair of shoes and three sets of custom inserts per year – at no out of pocket cost to them. Additionally, most private insurance companies will cover the same benefits as Elderfund.</p>
</section>

<section class="shoe-band abs">
  <h2 class="title">View All of Our Pebble Walk Co</h2>
  <h3 class="title">Women's and Men's Shoes</h3>
</section>
<section class="shoes abs">
  <div class="shoe abs" style="left:75px;top:60px"><div class="img" role="img" aria-label="Brown trail walking shoe" style="background:linear-gradient(160deg,#b08d66,#6e5438)"></div><b>Solvera - PW210 - Sand</b>Trail Walker - Lace</div>
  <div class="shoe abs" style="left:335px;top:60px"><div class="img" role="img" aria-label="Black casual dress shoe" style="background:linear-gradient(160deg,#444,#111)"></div><b>Solvera - PW318 - Jet</b>Casual Dress - Velcro</div>
  <div class="shoe abs" style="left:620px;top:60px"><div class="img" role="img" aria-label="Purple and grey trail shoe" style="background:linear-gradient(160deg,#8a5ab8,#4c3c6e)"></div><b>Solvera - PW210 - Sand</b>Trail Walker - Lace</div>
  <div class="shoe abs" style="left:900px;top:60px"><div class="img" role="img" aria-label="Black sporty shoe with velcro" style="background:linear-gradient(160deg,#555,#1a1a1a)"></div><b>Solvera - PW318 - Jet</b>Casual Dress - Velcro</div>
  <a class="btn abs" href="#" style="left:490px;top:295px;width:220px;height:58px;line-height:58px;font-size:17px">View All Shoes</a>
</section>

<section class="products abs">
  <svg class="abs" style="left:0;top:0" width="1200" height="80" viewBox="0 0 1200 80" preserveAspectRatio="none" aria-hidden="true"><path d="M0 0h1200v10Q600 120 0 10z" fill="#f4f5f6"/></svg>
  <h2 class="title abs">View All of Our Pebble Walk Co</h2>
  <h3 class="title abs">Elderfund Products</h3>
  <div class="round-photo abs" role="img" aria-label="Hand-held electrical nerve stimulator unit" style="left:80px;top:225px;width:210px;height:210px;background:radial-gradient(circle,#f4f6f8,#c9d3dc)"></div>
  <div class="product abs" style="left:310px;top:245px"><h4>TENS Unit</h4><p>A Transcutaneous Electrical Nerve Stimulator, or TENS Unit, is primarily used for managing chronic pain. It is a pocket size, portable.</p></div>
  <div class="round-photo abs" role="img" aria-label="Portable seat lift cushion" style="left:610px;top:225px;width:210px;height:210px;background:radial-gradient(circle,#2f3438,#9aa5ae)"></div>
  <div class="product abs" style="left:840px;top:245px"><h4>Seat Lift</h4><p>Electric powered portable seat assist can be used on most armchairs or sofas. Providing 100% lift, users enjoy the freedom of effortlessly rising.</p></div>
  <div class="dots abs" style="left:566px;top:468px"><span></span><span></span><span class="on" style="background:var(--green);border-color:var(--green)"></span></div>
</section>

<footer class="footer abs">
  <ul class="abs"><li>HOME</li><li>PEBBLE WALK CO! DO I QUALIFY</li><li>WHY DIABETIC SHOES</li><li>SHOES</li><li>PRODUCTS</li><li>SHOE FITTER JOBS</li><li>FAQ</li></ul>
  <div class="copy abs">© Pebble Walk Co. 2017 All Rights Reserved.</div>
  <div class="brand abs"><i class="dot" style="width:36px;height:36px"></i>Pebble Walk Co</div>
  <div class="socials abs"><i class="dot"></i><i class="dot"></i></div>
</footer>

</body>
</html>
```